"A Touch RMB" Business Card/Logo Design

I'm looking for a very creative look for my new business called "A Touch RMB" on a business card design. Don't be distracted by my "business card details" below....if you have other ideas on how you see "A Touch RMB" go for it. If probably should somehow give a look that I paint furniture....maybe a paint drip or something simple or you can get more creative....sky's the limit and I really need your creative eye on how to per tray that "A Touch RMB" means taking something old and turning into new again with some paint.

Industry/Entity Type

Business

Contact Information for Business Card

I refurbish and up-cycle furniture that needs "a little TLC'....thus, my business name was born called "A Touch RMB" (Those are my initials). I mainly paint old furniture of all styles and bring them back to life. I sometimes recreate furniture as well....I will make benches from old headboards of all sizes, etc. I'd love to see design that incorporate the crafty/creative side of me. If that means incorporating a paint brush, tools, paint cans, or furniture such as dressers, old vintage furniture, spindles, etc, etc. I don't know if something creative could be done with my initials (RMB). I really have a creative block of ideas and need your help bringing my "A Touch RMB" business to life.

P.S. Below is just one picture that I thought was neat and creative as they used a paintbrush but used spindles for the bristles and put their logo in the middle. Just an idea I thought was very unique and creative.

I'm very excited to see your design. Thank you for taking the time to create my logo/business card for me.

Carla

Requirements
Must have
• Please include this information on the card:
• My Name: Carla Brennick
• Address: 14706 318th Ln SE, Fox Hollow, MN 55418
• E-Mail: atouchrmb@mailcove.net
• FB: http:/www.friendpage.net/atouchrmb
• Cell: 763-419-7082

```html
<!DOCTYPE html>
<html lang="en">
<head>
<meta charset="utf-8">
<title>A Touch RMB — Business Card</title>
<link rel="stylesheet" href="https://fonts.googleapis.com/css2?family=Jost:wght@500&family=Source+Sans+3:wght@400;600&display=swap">
<style>
  :root {
    --stage-top: #2b2b2b;
    --stage-bottom: #050505;
    --card-white: #ffffff;
    --copper: #a6652a;
    --copper-text: #99561b;
    --cream: #f4e4cf;
    --ink: #141414;
  }
  * { margin: 0; padding: 0; box-sizing: border-box; }
  html, body { width: 1200px; height: 900px; overflow: hidden; }
  body {
    background: linear-gradient(180deg, var(--stage-top) 0%, #1a1a1a 45%, var(--stage-bottom) 100%);
    position: relative;
    font-family: "Source Sans 3", "Myriad Pro", sans-serif;
  }
  .card {
    position: absolute;
    top: 306px;
    width: 440px;
    height: 271px;
    border-radius: 12px;
  }
  .card-front { left: 149px; background: var(--card-white); }
  .card-back { left: 608px; background: var(--copper); }

  .brand-dot {
    position: absolute;
    left: 93px;
    top: 82px;
    width: 62px;
    height: 62px;
    border: 3px solid var(--copper-text);
    border-radius: 50%;
  }
  .wordmark {
    position: absolute;
    left: 0;
    width: 248px;
    top: 158px;
    text-align center;
    text-align: center;
    font-family: "Jost", "Futura", sans-serif;
    font-weight: 500;
    font-size: 28px;
    line-height: 34px;
    color: var(--ink);
    white-space: nowrap;
  }

  .details {
    position: absolute;
    left: 229px;
    top: 74px;
    color: var(--ink);
    font-size: 12.5px;
    line-height: 15px;
  }
  .holder-name {
    color: var(--copper-text);
    font-weight: 600;
    font-size: 16px;
    line-height: 20px;
    margin-bottom: 10px;
  }
  .address { margin-bottom: 12px; }
  .contact-list { list-style: none; }
  .contact-list li {
    display: flex;
    align-items: center;
    height: 16px;
  }
  .contact-list svg { width: 9px; height: 9px; margin: 0 6px 0 2px; flex: none; }

  .back-name {
    position: absolute;
    inset: 0;
    display: flex;
    align-items: center;
    justify-content: center;
    font-family: "Jost", "Futura", sans-serif;
    font-weight: 500;
    font-size: 30px;
    color: var(--cream);
  }
</style>
</head>
<body>
  <section class="card card-front">
    <span class="brand-dot" aria-hidden="true"></span>
    <div class="wordmark">A Touch RMB</div>
    <div class="details">
      <p class="holder-name">Carla Brennick</p>
      <p class="address">14706 318th Ln SE, Fox Hollow<br>MN 55418</p>
      <ul class="contact-list">
        <li>
          <svg viewBox="0 0 10 10" aria-hidden="true"><path d="M2 0.5 L3.6 2.4 L2.8 3.6 Q4 5.9 6.4 7.2 L7.6 6.4 L9.5 8 L8.4 9.5 Q4.5 9.3 1.8 6 Q0.2 3.6 0.5 1.6 Z" fill="var(--copper-text)"/></svg>
          763-419-7082
        </li>
        <li>
          <svg viewBox="0 0 10 10" aria-hidden="true"><rect x="0.5" y="2" width="9" height="6.5" fill="var(--copper-text)"/><path d="M0.8 2.3 L5 5.6 L9.2 2.3" stroke="#fff" stroke-width="0.9" fill="none"/></svg>
          atouchrmb@mailcove.net
        </li>
        <li>
          <svg viewBox="0 0 10 10" aria-hidden="true"><rect x="0.5" y="0.5" width="9" height="9" rx="1" fill="var(--copper-text)"/></svg>
          www.friendpage.net/atouchrmb
        </li>
      </ul>
    </div>
  </section>

  <section class="card card-back">
    <div class="back-name">A Touch RMB</div>
  </section>
</body>
</html>
```